Corporate Template

Looking for a set of corporate slides to be made which contain multiple different slides and orientations. Looking for at least 8 to 10 different master pages plus a Coversheet and closeout page. Incorporating a color palate similar to our logo coloring is preferred.

I have attached a logo.

```html
<!DOCTYPE html>
<html lang="en">
<head>
<meta charset="utf-8">
<title>Peoples &amp; Value</title>
<link rel="stylesheet" href="https://fonts.googleapis.com/css2?family=Arimo:wght@700&family=Tinos:wght@700&family=Great+Vibes&display=swap">
<style>
  :root {
    --bg-top: #0d3f7e;
    --bg-mid: #1566b8;
    --bg-bottom: #1c86de;
    --teal: #2fcfb6;
    --band: rgba(50, 50, 52, 0.88);
    --rail: #565656;
    --white: #ffffff;
    --footer: #ffffff;
    --ink-grey: #6a6a6a;
    --ink-blue: #1f6fb8;
    --rule: #9a9a9a;
  }
  * { margin: 0; padding: 0; box-sizing: border-box; }
  html, body { width: 1200px; height: 900px; overflow: hidden; background: #ffffff; }
  .slide {
    position: relative; width: 1200px; height: 900px; overflow: hidden;
    background: linear-gradient(180deg, var(--bg-top) 0%, var(--bg-mid) 45%, var(--bg-bottom) 100%);
    font-family: "Arimo", Arial, sans-serif; color: var(--white);
  }
  .rail { position: absolute; top: 0; right: 0; width: 35px; height: 825px; background: var(--rail); }
  .shapes { position: absolute; inset: 0; }
  .title { position: absolute; left: 766px; top: 50px; white-space: nowrap; font-weight: 400; }
  .title-script { font-family: "Great Vibes", cursive; font-size: 44px; }
  .title-bold { font-family: "Arimo", Arial, sans-serif; font-weight: 700; font-size: 41px; letter-spacing: -0.5px; }
  .value-label { position: absolute; font-weight: 700; font-size: 27px; text-align: center; letter-spacing: 0.3px; }
  .value-copy {
    position: absolute; font-family: "Tinos", "Times New Roman", serif; font-weight: 700;
    font-size: 22px; line-height: 23px; letter-spacing: 0.7px; white-space: nowrap;
  }
  .value-copy span { display: block; }
  .value-copy--right { text-align: right; }
  .photo {
    position: absolute; left: 681px; top: 512px; width: 484px; height: 313px;
    background: linear-gradient(100deg, #2a2a30 0%, #3c3a40 35%, #8d8a8c 60%, #c9b7a6 80%, #e4e8ee 100%);
    border-top-left-radius: 180px 120px;
    opacity: 0.92;
  }
  .footer { position: absolute; left: 0; top: 825px; width: 1200px; height: 75px; background: var(--footer); }
  .pager { position: absolute; left: 37px; top: 26px; font-weight: 700; font-size: 16px; color: var(--ink-grey); letter-spacing: 1px; }
  .pager .current { color: var(--ink-blue); font-size: 22px; }
  .brand { position: absolute; left: 680px; top: 28px; font-weight: 700; font-size: 16px; color: var(--ink-grey); letter-spacing: 0.5px; }
  .divider { position: absolute; left: 815px; top: 10px; width: 2px; height: 56px; background: var(--rule); }
  .url { position: absolute; left: 830px; top: 26px; font-family: "Tinos", "Times New Roman", serif; font-weight: 700; font-size: 18px; color: var(--ink-grey); }
</style>
</head>
<body>
<main class="slide">
  <div class="rail"></div>

  <svg class="shapes" width="1200" height="900" viewBox="0 0 1200 900" aria-hidden="true">
    <defs>
      <linearGradient id="orange" x1="0" y1="0" x2="0" y2="1">
        <stop offset="0" stop-color="#ff7a12"/><stop offset="1" stop-color="#e65800"/>
      </linearGradient>
      <linearGradient id="lime" x1="0" y1="0" x2="0" y2="1">
        <stop offset="0" stop-color="#b3c000"/><stop offset="1" stop-color="#eef528"/>
      </linearGradient>
      <linearGradient id="green" x1="0" y1="0" x2="0" y2="1">
        <stop offset="0" stop-color="#36d41f"/><stop offset="1" stop-color="#0da20a"/>
      </linearGradient>
      <linearGradient id="sky" x1="0" y1="0" x2="0" y2="1">
        <stop offset="0" stop-color="#2cb3f2"/><stop offset="1" stop-color="#128fd8"/>
      </linearGradient>
    </defs>
    <polygon class="title-flag" points="750,0 1062,0 919,152" fill="#2fcfb6"/>

    <polygon class="band" points="262,137 900,137 862,220 262,220" fill="rgba(50,50,52,0.88)"/>
    <polygon class="tag" points="0,137 269,137 296,178 269,220 0,220" fill="url(#orange)"/>

    <polygon class="band" points="350,272 1040,272 1000,352 350,352" fill="rgba(50,50,52,0.88)"/>
    <polygon class="tag" points="0,272 356,272 383,312 356,352 0,352" fill="url(#lime)"/>

    <polygon class="band" points="244,406 906,406 906,488 294,488" fill="rgba(50,50,52,0.88)"/>
    <polygon class="tag" points="906,406 1165,406 1165,488 906,488 880,447" fill="url(#green)"/>

    <polygon class="band" points="181,531 738,531 700,612 181,612" fill="rgba(50,50,52,0.88)"/>
    <polygon class="tag" points="0,531 181,531 208,571 181,612 0,612" fill="url(#sky)"/>
  </svg>

  <h1 class="title"><span class="title-script">Peoples</span><span class="title-bold">&amp;VALUE</span></h1>

  <div class="value-label" style="left:88px; top:162px; width:190px;">INTEGRITY</div>
  <p class="value-copy" style="left:295px; top:144px;">
    <span>We act with integrity in all of our business dealings.</span>
    <span style="padding-left:15px;">This is why we are relentless in taking the “high road”</span>
    <span>by practicing the highest business ethics standards.</span>
  </p>

  <div class="value-label" style="left:150px; top:297px; width:200px;">EXCELENCE</div>
  <p class="value-copy" style="left:380px; top:278px;">
    <span>We take pride in what we do. We strive to produce excellence</span>
    <span style="padding-left:15px;">from the smallest of details in our business to the largest.</span>
    <span>From start to finish we go for excellence.</span>
  </p>

  <p class="value-copy value-copy--right" style="right:321px; top:411px;">
    <span>By continually innovating we strive to produce sustainable</span>
    <span>solutions and values that consistently improve quality</span>
    <span>and performance to meet or exceed our clients standards.</span>
  </p>
  <div class="value-label" style="left:910px; top:431px; width:240px;">INNOVATION</div>

  <div class="value-label" style="left:20px; top:557px; width:160px;">RESULTS</div>
  <p class="value-copy" style="left:212px; top:537px;">
    <span>We’re a results-driven organization</span>
    <span>concentrating on meeting customer objectives,</span>
    <span>delivering on time at low cost with high quality</span>
  </p>

  <div class="photo" role="img" aria-label="Photograph of a team of five business people in suits standing in a row"></div>

  <footer class="footer">
    <div class="pager">1 | 2 | <span class="current">3</span> | 4 | 5 | 6 | 7 | 8 | 9</div>
    <div class="brand">CALDER GROUP</div>
    <div class="divider"></div>
    <div class="url">www.caldergroup.com</div>
  </footer>
</main>
</body>
</html>
```